High end business card design for custom homebuilding company

Looking for a high end business card design that is unique and elegant. Can use embossing, foil printing, laser die cutting, or any high end printing technique or high end paper. Will upload current design so you can see the logo and what we are using currently, but we want something more unique and elegant. I included our logo to help with design.

Target Market(s)

High end custom home buyers of $1.5 million plus homes. Also real estate developers of high end communities.

Industry/Entity Type

Business

Contact Information for Business Card

Double sided. We want something very elegant and expensive looking. We are looking to incorporate a combination of perhaps linen paper or a high end paper, with foil stamping or embossing/debossing to make the card look unique, but still elegant. We tend to use blacks and golds, but are open to any ideas. Looking for creative and unique design.

Colors

Designer to choose colors to be used in the design.

Requirements
Must have
• High end, elegant look. Can use foil, embossing, or high end papers like linen. We want to make the card unique and interesting, but elegant and expensive looking.
Nice to have
• I am including just some cards I saw that looked interesting for one reason or another. I like a clean elegant design and like both the clean white style, and the blacks. So not sure if we want a black design or white. Would like to see both.

```html
<!DOCTYPE html>
<html lang="en">
<head>
<meta charset="utf-8">
<title>Crestline Custom Homes – Business Card</title>
<link rel="stylesheet" href="https://fonts.googleapis.com/css2?family=Roboto:wght@300;400;700&display=swap">
<style>
  :root {
    --backdrop: #1b1b1b;
    --card: #232323;
    --card-shadow: rgba(0, 0, 0, 0.55);
    --text: #8c8c8c;
    --text-strong: #9d9d9d;
    --watermark: #2a2a2a;
    --brand: #b5b5b5;
  }
  * { margin: 0; padding: 0; box-sizing: border-box; }
  html, body {
    width: 1200px;
    height: 900px;
    overflow: hidden;
    background: var(--backdrop);
    font-family: "Roboto", sans-serif;
  }
  .canvas {
    position: relative;
    width: 1200px;
    height: 900px;
  }
  .card {
    position: absolute;
    background: var(--card);
    box-shadow: 0 4px 10px var(--card-shadow);
    overflow: hidden;
  }
  .card-front {
    left: 128px;
    top: 166px;
    width: 338px;
    height: 594px;
  }
  .card-back {
    left: 512px;
    top: 456px;
    width: 594px;
    height: 304px;
  }
  .contact {
    position: absolute;
    left: 44px;
    top: 56px;
    color: var(--text);
    z-index: 1;
  }
  .contact-name {
    font-size: 23px;
    font-weight: 300;
    color: var(--text-strong);
    line-height: 1;
    letter-spacing: 0.2px;
  }
  .contact-name strong { font-weight: 700; }
  .contact-role {
    font-size: 16px;
    font-weight: 400;
    margin-top: 6px;
  }
  .contact-rule {
    width: 22px;
    height: 2px;
    background: var(--text);
    margin: 12px 0 20px;
  }
  .contact-line {
    font-size: 13.5px;
    font-weight: 300;
    line-height: 1;
    margin-bottom: 13px;
  }
  .contact-address {
    font-size: 13.5px;
    font-weight: 400;
    line-height: 21px;
    margin-top: 2px;
  }
  .front-watermark {
    position: absolute;
    right: 28px;
    top: 20px;
    writing-mode: vertical-rl;
    font-size: 58px;
    font-weight: 300;
    letter-spacing: 4px;
    color: var(--watermark);
    text-transform: uppercase;
    white-space: nowrap;
  }
  .brand-lockup {
    position: absolute;
    left: 0;
    right: 0;
    top: 136px;
    display: flex;
    align-items: center;
    justify-content: center;
    gap: 14px;
  }
  .brand-dot {
    width: 14px;
    height: 14px;
    border-radius: 50%;
    background: var(--brand);
  }
  .brand-name {
    font-size: 27px;
    font-weight: 300;
    letter-spacing: 3px;
    color: var(--brand);
    text-transform: uppercase;
  }
</style>
</head>
<body>
<main class="canvas">
  <section class="card card-front" aria-label="Card front">
    <div class="front-watermark" aria-hidden="true">Crestline Homes</div>
    <div class="contact">
      <p class="contact-name"><strong>DALE</strong> MORGAN</p>
      <p class="contact-role">General Manager</p>
      <div class="contact-rule"></div>
      <p class="contact-line">555. 210. 4388 &nbsp;|&nbsp; 555. 306. 7192</p>
      <p class="contact-line">hello@crestlinehomes.example</p>
      <p class="contact-line">www.crestlinehomes.example</p>
      <p class="contact-address">Unit 4 12-16 Harbour Lane<br>Westvale, WA 6000</p>
    </div>
  </section>

  <section class="card card-back" aria-label="Card back">
    <div class="brand-lockup">
      <span class="brand-dot"></span>
      <span class="brand-name">Crestline Custom Homes</span>
    </div>
  </section>
</main>
</body>
</html>
```